Fernwick Digital Marketing Agency Website Design. I need a new website for my digital marketing agency. It needs to be FAST and easy to use. I want to be able to add videos to the main homepage like this page: https://www.lumatreeweb.example/search-marketing/cleveland-ohio-seo-companyI'd like to have the request quote tab on the top right side as well as my number above it. The following website is my favorite overall: http://www.vantorelgroup.example/ I'd love to copy something like that.

***** Website I want to copy: http://www.vantorelgroup.example/services/ ******
Updates

This needs to be a Wordpress website. Sorry for any confusion as this is the first time using MakerQuill. I need the homepage as described as well as a Services Page and Contact Us page. Services page should be simply yet creative with a spot for me to insert up to 8 services.

Target Market(s)

Business owners

Industry/Entity Type

Digital Marketing

Coding

Coded - Design and coding required

Number of Pages Required

3 page

Font styles to use
Other font styles liked:
• Oswald

Colors

Designer to choose colors to be used in the design.

Requirements
Must have
• I need to have a nice design/template to work off of in Wordpress. It needs to be bright and vibrant yet elegant in design.
Nice to have
• CTA at the top right as well as a place for the phone number. http://www.vantorelgroup.example/services/

```html
<!DOCTYPE html>
<html lang="en">
<head>
<meta charset="utf-8">
<title>Fernwick Digital Marketing Agency</title>
<link href="https://fonts.googleapis.com/css2?family=Oswald:wght@400;500;600;700&family=Open+Sans:wght@400;600;700&display=swap" rel="stylesheet">
<style>
:root{
  --orange:#f05a28;
  --orange-deep:#e2471a;
  --orange-soft:#f47a4c;
  --ink:#1b1b1b;
  --dark:#151515;
  --grey:#555;
  --line:#d9d9d9;
  --white:#fff;
}
*{box-sizing:border-box;margin:0;padding:0}
html,body{width:1200px;height:5325px;overflow:hidden}
body{font-family:"Open Sans",Arial,sans-serif;color:var(--ink);background:var(--white)}
.page{position:relative;width:1200px;height:5325px;overflow:hidden}
.abs{position:absolute}
.oswald{font-family:"Oswald",Arial,sans-serif}
.btn{position:absolute;display:flex;align-items:center;justify-content:center;font-family:"Oswald",Arial,sans-serif;color:var(--white);text-decoration:none}
.btn-solid{background:var(--orange);border-radius:4px}
.btn-ghost{border:2px solid var(--white);border-radius:4px;font-size:24px}

/* top bar */
.topbar{top:0;left:0;width:1200px;height:78px;background:var(--white);border-bottom:1px solid #eee}
.topbar .addr{left:95px;top:27px;font-size:14px;display:flex;align-items:center;gap:10px}
.topbar .phone{left:950px;top:14px;font-size:15px;display:flex;align-items:center;gap:10px}
.topbar .quote{left:965px;top:48px;width:146px;height:26px;font-size:15px}

/* header */
.header{top:78px;left:0;width:1200px;height:150px}
.brand{position:absolute;display:flex;align-items:center;gap:12px}
.brand-mark{width:34px;height:34px;background:var(--ink)}
.brand-name{font-family:"Oswald",Arial,sans-serif;font-weight:600;line-height:1}
.header .brand{left:95px;top:48px}
.header .brand-name{font-size:30px;color:var(--ink)}
.nav{position:absolute;left:764px;top:64px;display:flex;gap:42px;font-family:"Oswald",Arial,sans-serif;font-size:17px}

/* hero */
.hero{top:228px;left:0;width:1200px;height:650px;background:linear-gradient(120deg,#2d3844 0%,#4d5a66 40%,#3a4650 70%,#222c36 100%)}
.hero h1{left:124px;top:195px;font-size:58px;color:var(--white);font-weight:600}
.hero .lead{left:124px;top:270px;width:330px;color:var(--white);font-size:17px;line-height:1.4}
.hero .cta{left:124px;top:348px;width:324px;height:62px;font-size:24px}
.video{left:550px;top:138px;width:515px;height:290px;background:linear-gradient(135deg,#3b3f45,#6b6f75 60%,#2e3136);border-radius:4px}
.play{position:absolute;left:222px;top:110px}
.hero-curve{position:absolute;left:0;bottom:0}

/* intro */
.intro-img{left:90px;top:976px;width:425px;height:250px;background:linear-gradient(135deg,#c9cdd3,#7d858f 55%,#3e444c);border:4px solid #222}
.intro h2{position:absolute;left:557px;top:975px;width:560px;font-size:34px;line-height:1.25;font-weight:600}
.intro p{position:absolute;left:557px;top:1145px;width:560px;font-size:15.5px;line-height:1.5}

/* services */
.services{top:1306px;left:0;width:1200px;height:1738px;background:linear-gradient(180deg,var(--orange) 0%,var(--orange-soft) 50%,var(--orange) 100%)}
.services .title{position:absolute;left:0;width:1200px;top:72px;text-align:center;font-size:34px;font-weight:600;color:var(--white)}
.services .sub{position:absolute;left:300px;width:600px;top:138px;text-align:center;color:var(--white);font-size:15px;line-height:1.6}
.svc-img{position:absolute;width:425px;height:285px;border-radius:3px}
.svc-title{position:absolute;font-family:"Oswald",Arial,sans-serif;color:var(--white);font-size:33px;font-weight:600}
.svc-text{position:absolute;width:540px;color:var(--white);font-size:15px;line-height:1.55}
.svc-btn{width:206px;height:62px}

/* message */
.msg-img{left:578px;top:3152px;width:532px;height:416px;background:linear-gradient(135deg,#3d3f42,#8a8d91 50%,#2b2d30)}
.msg-card{left:90px;top:3170px;width:574px;height:280px;background:var(--white);box-shadow:0 4px 14px rgba(0,0,0,.25);border:1px solid #ccc}
.msg-card h2{position:absolute;left:22px;top:48px;font-size:33px;font-weight:600}
.msg-card p{position:absolute;left:22px;top:106px;width:500px;font-size:15.5px;line-height:1.55}
.msg-card .btn{left:22px;top:205px;width:148px;height:46px;font-size:18px}

/* faq */
.faq{top:3580px;left:0;width:1200px;height:630px;background:linear-gradient(180deg,#1d1d1d,#2c2c2c 50%,#1b1b1b)}
.faq h2{position:absolute;left:0;width:1200px;top:80px;text-align:center;color:var(--white);font-size:34px;font-weight:500}
.faq .intro-text{position:absolute;left:200px;width:800px;top:150px;text-align:center;color:var(--white);font-size:15.5px;line-height:1.55}
.faq-item{position:absolute;left:170px;width:856px;border:2px solid var(--white);color:var(--white);padding:12px 22px}
.faq-item h3{font-family:"Oswald",Arial,sans-serif;font-size:16px;font-weight:500;letter-spacing:.3px}
.faq-item p{font-size:15px;line-height:1.5;margin-top:12px;padding-left:18px}

/* contact */
.contact h2{position:absolute;left:0;width:1200px;top:4275px;text-align:center;font-size:36px;font-weight:500}
.contact .note{position:absolute;left:280px;width:640px;top:4340px;text-align:center;font-size:15.5px;line-height:1.55}
.ghost-name{position:absolute;left:0;top:4520px;width:1200px;text-align:center;font-family:"Oswald",Arial,sans-serif;font-weight:600;color:rgba(0,0,0,.05);line-height:1.05;white-space:nowrap}
.ghost-name .g1{display:block;font-size:110px}
.ghost-name .g2{display:block;font-size:74px}
.field{position:absolute;left:185px;width:460px;border:1px solid var(--line);background:rgba(255,255,255,.7);font-size:12px;padding:6px 8px;color:var(--ink)}
.contact .submit{left:185px;top:4817px;width:150px;height:44px;font-size:19px;border-radius:3px}
.info{position:absolute;left:788px;display:flex;align-items:flex-start;gap:20px;font-size:15.5px;line-height:1.5}
.follow{position:absolute;left:788px;top:4666px;display:flex;align-items:center;gap:16px;font-family:"Oswald",Arial,sans-serif;font-size:16px}
.follow span.sq{width:22px;height:22px;background:var(--orange)}

/* footer */
.footer{top:4915px;left:0;width:1200px;height:410px;background:#000;color:var(--white)}
.footer .brand{left:100px;top:110px}
.footer .brand-mark{background:var(--white)}
.footer .brand-name{font-size:28px;color:var(--white)}
.footer .tag{position:absolute;left:100px;top:160px;font-family:"Oswald",Arial,sans-serif;font-size:15px}
.fcol{position:absolute;top:105px}
.fcol h4{font-family:"Oswald",Arial,sans-serif;font-size:18px;font-weight:600;margin-bottom:14px}
.fcol li{list-style:none;font-size:14px;line-height:1.7}
.fcol p{font-size:14px;line-height:1.5;width:230px}
.news-input{margin-top:12px;width:230px;height:32px;background:var(--white);color:#555;font-size:12px;padding:8px}
.news-btn{position:relative;margin:14px 0 0 48px;width:104px;height:30px;font-size:16px;border-radius:3px}
.copy{position:absolute;left:0;width:1200px;top:352px;text-align:center;font-size:14px}
</style>
</head>
<body>
<div class="page">

  <!-- top bar -->
  <div class="abs topbar">
    <div class="abs addr">
      <svg width="14" height="18" viewBox="0 0 14 18"><path d="M7 0C3 0 0 3 0 7c0 5 7 11 7 11s7-6 7-11c0-4-3-7-7-7z" fill="#1b1b1b"/><circle cx="7" cy="7" r="2.5" fill="#fff"/></svg>
      2270 Harrow Brook Dr Maple Crest, OH 45917
    </div>
    <div class="abs phone">
      <svg width="16" height="16" viewBox="0 0 24 24"><path d="M6.6 10.8a15 15 0 006.6 6.6l2.2-2.2a1 1 0 011-.25 11 11 0 003.5.56 1 1 0 011 1V20a1 1 0 01-1 1A17 17 0 013 4a1 1 0 011-1h3.5a1 1 0 011 1 11 11 0 00.56 3.5 1 1 0 01-.25 1z" fill="#1b1b1b"/></svg>
      +1 440-555-0142
    </div>
    <a class="btn btn-solid quote">Request Quote</a>
  </div>

  <!-- header -->
  <header class="abs header">
    <div class="brand"><span class="brand-mark"></span><span class="brand-name">Fernwick</span></div>
    <nav class="nav"><span>Home</span><span>Services</span><span>Blog</span><span>Contact Us</span><span>FAQ</span></nav>
  </header>

  <!-- hero -->
  <section class="abs hero" role="img" aria-label="Background photo of a growth concept with plants and coins">
    <h1 class="abs oswald">GROW</h1>
    <p class="abs lead">This Is All About Your Company Growing Online. End Of Story.</p>
    <a class="btn btn-solid cta">Grow My Company Now</a>
    <div class="abs video" role="img" aria-label="Video thumbnail about SEO">
      <svg class="play" width="72" height="72" viewBox="0 0 72 72"><circle cx="36" cy="36" r="33" fill="none" stroke="#fff" stroke-width="4"/><path d="M28 22l22 14-22 14z" fill="#fff"/></svg>
    </div>
    <svg class="hero-curve" width="1200" height="90" viewBox="0 0 1200 90" preserveAspectRatio="none"><path d="M0 40 Q600 150 1200 0 L1200 90 L0 90z" fill="#fff"/></svg>
  </section>

  <!-- intro -->
  <section class="intro">
    <div class="abs intro-img" role="img" aria-label="Photo of a laptop on an office desk"></div>
    <h2 class="oswald">Seo Company In Cleveland, Ohio - Search Engine Optimization Services For Local Businesses In Ohio</h2>
    <p>Watch the Video Testimonial below from our client, the owner of one of Cleveland's and Akron's top Electrician Companies!<br>We love local businesses and want yours to grow like his business!</p>
  </section>

  <!-- services -->
  <section class="abs services">
    <h2 class="title oswald">SERVICES</h2>
    <p class="sub">Having partnered with hundreds of businesses in northern Ohio, our team of digital marketing experts have a proven method to drive revenue growth.</p>

    <div class="svc-img" style="left:90px;top:308px;background:linear-gradient(135deg,#e8e4d8,#c9d36a 50%,#d9d2c4)" role="img" aria-label="Photo of a content marketing word sketch on paper"></div>
    <h3 class="svc-title" style="left:580px;top:300px">CONTENT MARKETING</h3>
    <p class="svc-text" style="left:580px;top:372px">Content marketing is a strategic approach to utilizing and executing different kinds of content to reach your audience. Distribution methods are just as important as content creation. We strategize to reach your followers where they are most comfortable.</p>
    <a class="btn btn-ghost svc-btn" style="left:580px;top:520px">Learn More</a>

    <h3 class="svc-title" style="left:90px;top:688px">SEARCH OPTIMIZATION</h3>
    <p class="svc-text" style="left:90px;top:760px">Search Engine Optimization (SEO) is more than just a trending topic, it's a huge component to your online success. Fernwick knows what it takes to rank organically on search engines. We stay on top of evolving SEO trends so you don't have to.</p>
    <a class="btn btn-ghost svc-btn" style="left:90px;top:910px">Learn More</a>
    <div class="svc-img" style="left:685px;top:694px;background:linear-gradient(135deg,#f2f2f2,#bfc4c9 50%,#8d949b)" role="img" aria-label="Photo of a laptop showing an SEO diagram"></div>

    <div class="svc-img" style="left:90px;top:1134px;background:linear-gradient(135deg,#0f3b4c,#2c8099 50%,#0c2f3d)" role="img" aria-label="Photo of lead generation icons on a digital screen"></div>
    <h3 class="svc-title" style="left:580px;top:1126px">LEAD GENERATION</h3>
    <p class="svc-text" style="left:580px;top:1198px">Gaining qualified leads allows you to have an open dialogue with valuable potential customers. Whether you market a case study, white paper, product specific email or a free consultation, we work to leverage your services to target your ideal demographic.</p>
    <a class="btn btn-ghost svc-btn" style="left:580px;top:1356px">Learn More</a>

    <a class="btn btn-ghost" style="left:477px;top:1587px;width:246px;height:70px">View More</a>
  </section>

  <!-- message -->
  <div class="abs msg-img" role="img" aria-label="Photo of a tablet showing digital marketing graphics"></div>
  <section class="abs msg-card">
    <h2 class="oswald">YOUR MAIN MESSAGE</h2>
    <p>Use this space to tell people what your company does and why and how it does it. What're you known for? Who likes you? What's your number one competitive advantage?</p>
    <a class="btn btn-solid">Read More</a>
  </section>

  <!-- faq -->
  <section class="abs faq">
    <h2 class="oswald">FREQUENTLY ASKED QUESTIONS (FAQ)</h2>
    <p class="intro-text">This is where you should answer the most common questions prospective customers might have. It's a good idea to cover things like your return policy, product warranty info, shipping and returns, etc. Check out the examples below</p>
    <div class="faq-item" style="top:293px;height:131px">
      <h3>–&nbsp; WHAT'S YOUR RETURN POLICY?</h3>
      <p>Return any of our products–no questions asked–within 30 days of purchase. We even pay return shipping.</p>
    </div>
    <div class="faq-item" style="top:435px"><h3>+&nbsp; DO YOU SHIP OVERSEES AND TO P.O. BOXES?</h3></div>
    <div class="faq-item" style="top:492px"><h3>+&nbsp; DO YOU HAVE CUSTOMER SERVICE?</h3></div>
  </section>

  <!-- contact -->
  <section class="contact">
    <div class="ghost-name"><span class="g1">Fernwick</span><span class="g2">Digital Marketing Agency</span></div>
    <h2 class="oswald">Contact Us</h2>
    <p class="note">Get in touch and we'll get back to you as soon as we can. We look forward to hearing from you!</p>
    <div class="field" style="top:4433px;height:40px">Name</div>
    <div class="field" style="top:4490px;height:40px">Email</div>
    <div class="field" style="top:4558px;height:150px">Message</div>
    <div class="field" style="top:4725px;height:40px">What is Thirteen Minus 6? *</div>
    <a class="btn btn-solid submit">Submit</a>

    <div class="info" style="top:4470px">
      <svg width="20" height="16" viewBox="0 0 20 16"><rect width="20" height="16" rx="2" fill="#f05a28"/><path d="M1 2l9 7 9-7" fill="none" stroke="#fff" stroke-width="1.6"/></svg>
      hello@fernwick.example
    </div>
    <div class="info" style="top:4528px">
      <svg width="18" height="18" viewBox="0 0 24 24"><path d="M6.6 10.8a15 15 0 006.6 6.6l2.2-2.2a1 1 0 011-.25 11 11 0 003.5.56 1 1 0 011 1V20a1 1 0 01-1 1A17 17 0 013 4a1 1 0 011-1h3.5a1 1 0 011 1 11 11 0 00.56 3.5 1 1 0 01-.25 1z" fill="#f05a28"/></svg>
      440-555-0187
    </div>
    <div class="info" style="top:4584px">
      <svg width="16" height="20" viewBox="0 0 14 18"><path d="M7 0C3 0 0 3 0 7c0 5 7 11 7 11s7-6 7-11c0-4-3-7-7-7z" fill="#f05a28"/><circle cx="7" cy="7" r="2.5" fill="#fff"/></svg>
      <span>2270 Harrow Brook<br>Dr Maple Crest, OH 45917</span>
    </div>
    <div class="follow">Follow us: <span class="sq"></span></div>
  </section>

  <!-- footer -->
  <footer class="abs footer">
    <div class="brand"><span class="brand-mark"></span><span class="brand-name">Fernwick</span></div>
    <div class="tag">Digital Marketing Agency</div>
    <div class="fcol" style="left:465px">
      <h4>Quick Link</h4>
      <ul><li>Home</li><li>Services</li><li>Blog</li><li>Contact Us</li><li>Faq</li></ul>
    </div>
    <div class="fcol" style="left:621px">
      <h4>Services</h4>
      <ul><li>Content Marketing</li><li>Search Optimization</li><li>Lead Generation</li><li>Web Development</li><li>Social Media</li></ul>
    </div>
    <div class="fcol" style="left:824px">
      <h4>NewsLetter</h4>
      <p>Email newsletters are a powerful accounting firm</p>
      <div class="news-input">Enter the email</div>
      <a class="btn btn-solid news-btn">Send</a>
    </div>
    <p class="copy">© 2019 Fernwick. All Rights Reserved</p>
  </footer>

</div>
</body>
</html>
```